Homepage web design

I need a homepage design that will be easy to build into a default Word Press theme. Basically, header, navigation, body with sidebar, and footer.

This website is for a small commercial real estate firm in the Washington DC, Maryland and Virginia market.

THIS IS NOT A HOUSING/RESIDENTIAL WEBSITE. PLEASE DO NOT ADD ANY PROPERTY SEARCH FUNCTIONALITY.

Target Market(s)

People looking for basic information about the team and services provided.

Industry/Entity Type

Real Estate

Requirements
Must have
• Professional look. Clean design.

```html
<!DOCTYPE html>
<html lang="en">
<head>
<meta charset="utf-8">
<title>Meridian Realty Brokerage — Home</title>
<link rel="stylesheet" href="https://fonts.googleapis.com/css2?family=Arimo:wght@400;700&family=Roboto+Slab:wght@400&display=swap">
<style>
:root{
  --page:#f4f3f1;
  --topbar:#4a4a4a;
  --green:#8aab0e;
  --green-dark:#6f8c06;
  --brand:#1a8a4a;
  --band:#3e3e3e;
  --sidebar:#e6e5e3;
  --ink:#222;
  --muted:#9a9a9a;
  --line:#dcdcdc;
  --white:#fff;
}
*{box-sizing:border-box;margin:0;padding:0}
html,body{width:692px;height:1200px;overflow:hidden}
body{position:relative;background:var(--page);font-family:"Arimo",Arial,sans-serif;color:var(--ink)}
.abs{position:absolute}
.topbar{left:0;top:0;width:692px;height:5px;background:var(--topbar)}
.header{left:0;top:5px;width:692px;height:95px;border-bottom:1px solid var(--line)}
.logo{left:68px;top:22px;color:var(--brand);font-weight:700;font-family:"Arimo",Arial,sans-serif}
.logo .mark{font-size:34px;line-height:34px;letter-spacing:1px}
.logo .sub{font-size:5.5px;letter-spacing:.3px;margin-top:3px}
.search{left:505px;top:34px;width:112px;height:19px;background:var(--white);border:1px solid #e6e6e6;font-size:8px;color:#aaa;padding:4px 0 0 18px}
.search svg{position:absolute;left:5px;top:4px}
.nav{left:70px;top:83px;display:flex;font-size:8px;color:#333}
.nav span{margin-right:20px}
.hero{left:68px;top:119px;width:549px;height:211px;background:linear-gradient(180deg,#2a4fa8 0%,#3a5f9e 35%,#6b4a2a 70%,#2b2a25 100%)}
.band{left:0;top:330px;width:692px;height:134px;background:var(--band)}
.welcome{left:83px;top:343px;width:345px;color:var(--white)}
h2{font-size:9px;letter-spacing:2px;font-weight:700;text-transform:uppercase}
.welcome p{margin-top:12px;font-size:8px;line-height:10.5px;color:#a9a9a9}
.btn{display:inline-block;background:var(--green);color:var(--white);font-size:6.5px;font-weight:700;padding:7px 10px;margin-top:12px;border-radius:2px}
.why{left:437px;top:240px;width:180px;height:224px;background:var(--green);color:var(--white);padding:14px 17px}
.why p{margin-top:12px;font-size:7px;line-height:9.2px}
.why ul{list-style:none;margin-top:16px;margin-left:12px}
.why li{font-size:7px;margin-bottom:8.5px;display:flex;align-items:center}
.why li svg{margin-right:7px}
.sidebar{left:437px;top:464px;width:180px;height:518px;background:var(--sidebar)}
.main-photo{left:56px;top:479px;width:364px;height:123px;background:linear-gradient(180deg,#3d6fb8 0%,#7a8fa8 40%,#3b3328 70%,#4aa0b0 100%)}
.about{left:56px;top:612px;width:364px}
.about h2,.side h2{color:var(--ink)}
.body-text{font-size:7px;line-height:9.3px;color:var(--muted)}
.about .body-text{margin-top:8px}
.ad-art{left:56px;top:672px;width:168px;height:95px;background:linear-gradient(180deg,#2c2440 0%,#7a4a6a 55%,#c76a8a 100%)}
.quick{left:234px;top:672px;width:185px;font-size:7.5px;line-height:10.5px;color:#333}
.quick-muted{left:236px;top:742px;width:183px}
.lower{left:56px;top:789px;width:364px}
.quote{left:56px;top:829px;width:364px;color:var(--brand);font-size:10px;letter-spacing:1.2px;line-height:12px;text-transform:uppercase}
.side h2{left:451px;top:478px}
.post{left:451px;width:160px;display:flex}
.thumb{width:60px;height:40px;flex:none;background:linear-gradient(180deg,#6a8ab8,#8a6a40)}
.post .body-text{margin-left:6px;font-size:6.5px;line-height:8.6px}
.post b{font-weight:400;color:var(--ink);font-size:7px}
.gallery{left:447px;top:684px;width:155px;display:grid;grid-template-columns:74px 74px;gap:7px 6px}
.gallery div{height:47px;background:linear-gradient(180deg,#2c3a55,#6a5a45)}
.gallery div:nth-child(n+3){background:linear-gradient(180deg,#a88a60,#6a4a30)}
.ad-label{left:451px;top:805px;font-size:8px;letter-spacing:2px;color:#cfcfcf;font-weight:700}
.ad{left:447px;top:826px;width:152px;height:126px;background:linear-gradient(160deg,#3a3f46 0%,#2a2e33 60%,#b52030 100%)}
.signup{left:156px;top:1000px;display:flex;align-items:center;font-family:"Roboto Slab",Georgia,serif;font-size:9px;color:#333}
.signup .field{width:150px;height:21px;background:var(--white);border:1px solid #ddd;margin:0 11px 0 11px}
.signup .go{background:var(--green);color:var(--white);font-size:7.5px;padding:5px 7px}
.footer{left:0;top:1046px;width:692px;height:120px;background:var(--green);color:var(--white)}
.fcol{position:absolute;top:22px}
.fcol h2{font-size:7px}
.fcol ul{list-style:none;margin-top:12px;margin-left:7px;font-size:6.5px;font-weight:700;line-height:10px}
.flogo{left:522px;top:48px;width:96px;height:61px;background:var(--white);color:var(--brand);font-weight:700;text-align:center;padding-top:12px}
.flogo .mark{font-size:26px;line-height:26px}
.flogo .sub{font-size:4.5px;margin-top:3px}
.bottom{left:62px;top:1174px;font-size:6.5px;color:#777;line-height:8.5px}
.social{left:506px;top:1178px;display:flex}
.social span{width:9px;height:9px;border-radius:50%;background:#9a9a9a;margin-right:17px}
</style>
</head>
<body>
<div class="abs topbar"></div>
<header class="abs header"></header>
<div class="abs logo"><div class="mark">MRB</div><div class="sub">MERIDIAN REALTY BROKERAGE</div></div>
<div class="abs search"><svg width="9" height="9" viewBox="0 0 9 9"><circle cx="5.5" cy="3.5" r="2.6" fill="none" stroke="#8aab0e" stroke-width="1.2"/><line x1="3.6" y1="5.4" x2="1" y2="8" stroke="#8aab0e" stroke-width="1.4"/></svg>search</div>
<nav class="abs nav"><span style="margin-right:12px">Home</span><span>About Us</span><span>Services</span><span>Buying</span><span>Selling</span><span>Properties</span><span>Our Team</span><span>Enquriy</span><span>Contact Us</span></nav>

<div class="abs hero" role="img" aria-label="Modern villa with curved roof lit at dusk"></div>
<div class="abs band"></div>
<section class="abs welcome">
  <h2>Welcome to MRB</h2>
  <p>Autem exerci vidtarget mirum ea etiam. Lectores formas volutpat ea feugait litterarum. Quod imperdiet consuetud ium decima typi fiant. Adipiscing duis putamus quod in videntur. Ii adipis cing illum legere nulla lobortis. Iriure ea ullamcorper ii tation et.</p>
  <span class="btn">KNOW MORE</span>
</section>
<section class="abs why">
  <h2>Why choose us?</h2>
  <p>Autem exerci videntur mirum ea etiam. Lectores formas volutpat ea feugait lit terarum. Quod imperdiet consuetud iu decima typi fiant. Adipi scing duis puta mus quod in videntur. Ii adipis cing illum legere nulla lobortis. Irure ea ullam corper ii tation et.</p>
  <ul>
    <li><svg width="8" height="8" viewBox="0 0 8 8"><circle cx="4" cy="4" r="4" fill="#fff"/><path d="M2 4.2l1.4 1.3L6 2.8" fill="none" stroke="#8aab0e" stroke-width="1.2"/></svg>Autem exerci videntur mirum ea etiam.</li>
    <li><svg width="8" height="8" viewBox="0 0 8 8"><circle cx="4" cy="4" r="4" fill="#fff"/><path d="M2 4.2l1.4 1.3L6 2.8" fill="none" stroke="#8aab0e" stroke-width="1.2"/></svg>Lectores formas volutpat ea feugai</li>
    <li><svg width="8" height="8" viewBox="0 0 8 8"><circle cx="4" cy="4" r="4" fill="#fff"/><path d="M2 4.2l1.4 1.3L6 2.8" fill="none" stroke="#8aab0e" stroke-width="1.2"/></svg>Frmas volutpat ea feugai</li>
    <li><svg width="8" height="8" viewBox="0 0 8 8"><circle cx="4" cy="4" r="4" fill="#fff"/><path d="M2 4.2l1.4 1.3L6 2.8" fill="none" stroke="#8aab0e" stroke-width="1.2"/></svg>Lectores formas volutpat ea feugai</li>
  </ul>
</section>

<div class="abs sidebar"></div>
<div class="abs main-photo" role="img" aria-label="Resort pool with thatched pavilion at dusk"></div>
<section class="abs about">
  <h2>About our company</h2>
  <p class="body-text">Autem exerci videntur mirum ea etiam. Lectores formas volutpat ea feugait litterarum. Quod imperdiet consuetud ium decima typi fiant. Adipiscing duis putamus quod in videntur. Ii adipiscing illum legere nulla lobortis. Iriure ea ullamcorper ii tation et.</p>
</section>
<div class="abs ad-art" role="img" aria-label="Promotional artwork for Blue Shore, a misty lake at sunset"></div>
<p class="abs quick">This is a quick example of the left sidebar page template, you can of course choose from full width, left or right sidebar when creating any page or any post – couple this with columns, shortcodes and lightboxes and it's almost limitless layout control!</p>
<p class="abs body-text quick-muted">Autem exerci videntur mirum ea etiam. Lectores formas ium decima typi fiant. Adipiscing duis putamus quod</p>
<p class="abs body-text lower">Autem exerci videntur mirum ea etiam. Lectores formas volutpat ea feugait litterarum. Quod imperdiet consuetud ium decima typi fiant. Adipiscing duis putamus quod in videntur. Ii adipiscing illum legere nulla lobortis. Iriure ea ullamcorper ii tation et.</p>
<p class="abs quote">The secret to life, as I was once told, is to believe in yourself and.. crap can't remember the rest</p>

<aside class="side">
  <h2 class="abs" style="left:451px;top:478px">Recent postings</h2>
  <div class="abs post" style="top:496px"><div class="thumb" role="img" aria-label="Modern house exterior"></div><p class="body-text">Autem exerci videntur mirum ium decima typi fiant. Adipis ullamcorper ii tation et.<br><b>Read more..</b></p></div>
  <div class="abs post" style="top:547px"><div class="thumb" role="img" aria-label="House with garden terrace"></div><p class="body-text">Autem exerci videntur mirum ium decima typi fiant. Adipis ullamcorper ii tation et.<br><b>Read more..</b></p></div>
  <div class="abs post" style="top:598px"><div class="thumb" role="img" aria-label="House lit at night"></div><p class="body-text">Autem exerci videntur mirum ium decima typi fiant. Adipis ullamcorper ii tation et.<br><b>Read more..</b></p></div>
  <h2 class="abs" style="left:451px;top:663px">Gallery</h2>
  <div class="abs gallery">
    <div role="img" aria-label="Villa exterior at night"></div>
    <div role="img" aria-label="Villa facade at dusk"></div>
    <div role="img" aria-label="Dining room interior"></div>
    <div role="img" aria-label="Living room interior"></div>
  </div>
  <div class="abs ad-label">ADVERTISEMENT</div>
  <div class="abs ad" role="img" aria-label="Advertisement for a free user interface kit download"></div>
</aside>

<div class="abs signup">Sign up for our e-newsletter!<span class="field"></span><span class="go">Get Involved</span></div>

<footer class="abs footer">
  <div class="fcol" style="left:70px"><h2>About us</h2><ul><li>About Us</li><li>Blog</li><li>News</li><li>Vision and Mission</li><li>Our Accountability</li><li>Financials</li></ul></div>
  <div class="fcol" style="left:189px"><h2>Our friends</h2><ul><li>Green Earth Fund</li><li>Helpinghands.org</li><li>Clear Springs</li><li>Bright Hope Foundation</li><li>Wildlands.org</li><li>Pawcare.org</li></ul></div>
  <div class="abs flogo"><div class="mark">MRB</div><div class="sub">MERIDIAN REALTY BROKERAGE</div></div>
</footer>
<div class="abs bottom">COPYRIGHT 2013. ALL RIGHTS RESERVED.<br>TERMS &amp; CONDITIONS &nbsp;-&nbsp; PRIVACY &nbsp;-&nbsp; DISCLAIMER</div>
<div class="abs social"><span></span><span></span><span></span><span></span><span></span></div>
</body>
</html>
```